Vorlen - Customer Experience Software Company Web Design

*****UPDATE*****
We've been getting a lot of corporate designs through. Unfortunately this is not what we are looking for. We would like our brand to be more approachable and for the look and feel to to be a bit more fun.
Also the best designs we have received so far have followed the "less is more" approach. Im hoping any news designs will take these aspects into account.
*****************

Background:

Vorlen is a Customer Experience Technology company. We equip business and technology teams with the frameworks, tools and services to help them create compelling experiences for their customers.

Our flagship product - Vorlen CX is an open-source customer experience application framework – it enables organisation to build highly differentiated business applications to deliver compelling experiences to your customers.

Vorlen CX is designed for innovators who understand that unlocking opportunity in today’s competitive marketplace is driven by delivering a better customer experience.

Task:

We are looking for a web design (we need PSD, no HTML/CSS) for our company site through which to launch our customer experience framework product. The site will be also used as a support site, so the functional aspect of the site is as important as the visual impact for sales.

In order to help us conceptualise ideas and content we have drafted a temporary website using a standard wordpress theme (please see details below). Now we have a general idea of our requirements we like we would like to take it to the next level and get some designs with that professional edge.

Our target market are Enterprise organisations - that is senior members of the business & technology teams (Business General Managers, CTO’s, CIO’s, and Senior Architects and Senior Developers). We want something clean & fresh which is DIFFERENT from the typical corporate technology websites out there. We would like to be seen as more approachable than most large technology companies.

Words we would like to use to describe the finished design:
• Clean (we’re thinking white background with one or two key colours)
• Fresh
• Light
• Modern
• Less is more
• Web 2.0
• Fun but professional (aimed at Enterprise/Large organisations)
• Bold, clear call to action – e.g. Live Demo & Download
• Readable (but Sans Serif)

As we’re a Customer Experience company, the usability of the site is critical. The site must be functional, intuitive & easy to navigate. We want to keep the number of user clicks to the bare minimum possible.

Other aspects, which we would like to incorporate into the site
• Home Page banner slider
• Client logon
• Newsletter sign up
• Social media links – Chatterbook, Linkfolk (for starters)
• Rich footer links

Some websites we like
• http://brightpanelworks.example - clean, light, modern & intuitive
• http://www.tamsoledrik.example - bold, clear messaging
• http://www.opengridhub.example/markup/emblem - punchy, colourful
• http://postwren.example/ - modern, clear messaging, colourful, rich footer area

Target Market(s)

Enterprise organisations - that is senior members of the business & technology teams (Business General Managers, CTO’s, CIO’s, Senior Devs)

Industry/Entity Type

Business

Requirements
Must have
• - Design Specs: Accepted file formats: During the design phase adobe PSD or JPEG are OK (if you need to upload files), but for the handover we'll need PSD only with all the original layers.
- The width needs to be a size that will work with every size computer screen
- Need to use cross-platform compatible font
- The graphic elements used for the design must be copyright free

Current test site
- URL http://vorlen.example/wp-admin
- username: artmarket
- password: artmarket

IMPORTANT NOTE REGARDING OUR CURRENT TEST SITE:

This is a very basic version of a site to help us generate requirements. This design is only a starting point/input and is not locked in stone i.e. we do not simply want this site simply tweaked around the edges.

We are looking for you to use all of your graphic design skills and experience to create a truly awesome site design!

```html
<!DOCTYPE html>
<html lang="en">
<head>
<meta charset="utf-8">
<title>Vorlen – Customer Experience Application Framework</title>
<link rel="stylesheet" href="https://fonts.googleapis.com/css2?family=Arimo:wght@400;700&family=Federo&family=Graduate&display=swap">
<style>
:root{
  --page:#e3e3e3;
  --header-top:#f6f6f6;
  --header-bottom:#d9d9d9;
  --stage:#555555;
  --stage-edge:#2f2f2f;
  --ink:#222222;
  --ink-soft:#444444;
  --heading:#4e4e4e;
  --muted:#8a8a8a;
  --rule:#c9c9c9;
  --btn-top:#fbfbfb;
  --btn-bottom:#dedede;
  --btn-line:#a9a9a9;
  --frame:#eef0f4;
  --frame-bar:#c3cad6;
  --dot:#2d3340;
  --social:#3b6fb0;
}
*{box-sizing:border-box;margin:0;padding:0}
html,body{width:1098px;height:1200px;overflow:hidden}
body{background:var(--page);font-family:"Arimo",Arial,sans-serif;color:var(--ink);position:relative}
.site-header{position:absolute;left:0;top:0;width:1098px;height:44px;background:linear-gradient(var(--header-top),var(--header-bottom));border-bottom:1px solid #bdbdbd}
.brand{position:absolute;left:41px;top:9px;font-family:"Arimo",Arial,sans-serif;font-weight:700;font-size:21px;color:var(--ink);letter-spacing:.5px}
.nav-pill{position:absolute;top:12px;height:22px;border:1px solid var(--btn-line);border-radius:6px;background:linear-gradient(var(--btn-top),var(--btn-bottom));font-size:10px;font-weight:700;line-height:20px;text-align:center;color:var(--ink)}
.nav-pill.is-current{color:var(--muted)}
.nav-account{position:absolute;top:17px;font-size:10px;color:var(--muted)}
.stage{position:absolute;left:0;top:44px;width:1098px;height:348px;background:var(--stage)}
.stage-edge{position:absolute;left:0;top:392px;width:1098px;height:11px;background:var(--stage-edge)}
.slider{position:absolute;left:211px;top:76px;width:676px;height:291px;background:var(--frame);border:1px solid #8d939d;border-radius:5px;box-shadow:0 2px 6px rgba(0,0,0,.4)}
.slide-art{position:absolute;left:4px;top:4px;width:666px;height:244px;border-radius:4px;background:radial-gradient(ellipse at 30% 40%,#2a1a3a 0%,#050505 45%),#000}
.slider-bar{position:absolute;left:4px;top:250px;width:666px;height:34px;background:linear-gradient(#e4e8ee,var(--frame-bar));border-radius:0 0 4px 4px}
.slider-dots{position:absolute;right:18px;top:13px;display:flex;gap:8px}
.slider-dots span{width:9px;height:9px;border-radius:50%;background:var(--dot)}
.tagline{position:absolute;left:0;top:415px;width:1098px;text-align:center;font-family:"Graduate",Georgia,serif;font-variant:small-caps;font-size:60px;line-height:72px;color:var(--heading)}
.cta{position:absolute;left:135px;top:720px}
.cta-btn{position:absolute;top:0;height:32px;border:1px solid var(--btn-line);border-radius:7px;background:linear-gradient(var(--btn-top),var(--btn-bottom));font-weight:700;font-size:16px;line-height:30px;text-align:center;color:var(--ink)}
.cta-note{position:absolute;left:8px;top:44px;width:240px;font-size:11px;line-height:15px;font-variant:small-caps;color:var(--ink)}
.cta-note u{font-weight:700}
.divider{position:absolute;left:395px;top:615px;width:1px;height:351px;background:var(--rule)}
.features{position:absolute;left:420px;top:614px;width:515px}
.feature-title{font-family:"Federo",Georgia,sans-serif;font-weight:400;color:var(--ink)}
.feature-title.lead{font-size:28px;line-height:34px}
.feature-title.sub{font-size:19px;line-height:26px;margin-top:14px}
.feature-text{font-size:9.6px;line-height:12px;color:var(--ink-soft);margin-top:14px}
.site-footer{position:absolute;left:0;top:1037px;width:1098px;height:163px;border-top:1px solid #f4f4f4;box-shadow:0 -1px 0 #cfcfcf}
.footer-col{position:absolute;top:18px}
.footer-col h3{font-family:"Arimo",Arial,sans-serif;font-weight:400;font-size:20px;color:var(--ink-soft);line-height:24px}
.footer-col ul{list-style:none;margin-top:2px}
.footer-col li{font-size:11.5px;line-height:14.6px;color:var(--ink-soft)}
.subscribe-field{position:absolute;left:0;top:28px;width:236px;height:21px;background:#fff;border:1px solid #d6d6d6;font-size:9px;line-height:19px;padding-left:12px;color:#555}
.subscribe-btn{position:absolute;left:0;top:56px;width:71px;height:20px;border:1px solid var(--btn-line);border-radius:6px;background:linear-gradient(var(--btn-top),var(--btn-bottom));font-size:9.5px;line-height:18px;text-align:center;color:var(--ink-soft)}
.social{display:flex;gap:12px;margin-top:8px}
.social-link{display:flex;align-items:center;gap:4px;font-size:11px;color:var(--ink-soft)}
.social-link i{width:14px;height:14px;background:var(--social);border-radius:2px;display:block}
</style>
</head>
<body>
<header class="site-header">
  <div class="brand">Vorlen</div>
  <div class="nav-pill is-current" style="left:567px;width:58px">HOME</div>
  <div class="nav-pill" style="left:635px;width:69px">PRODUCTS</div>
  <div class="nav-pill" style="left:716px;width:67px">SUPPORT</div>
  <div class="nav-pill" style="left:795px;width:59px">BLOG</div>
  <div class="nav-pill" style="left:865px;width:59px">ABOUT</div>
  <div class="nav-account" style="left:946px">SIGN UP</div>
  <div class="nav-account" style="left:1001px">LOG IN</div>
</header>

<section class="stage">
</section>
<div class="stage-edge"></div>
<div class="slider">
  <div class="slide-art" role="img" aria-label="Banner slide: a desktop monitor beside a colourful 3D bar chart and pie chart on black"></div>
  <div class="slider-bar">
    <div class="slider-dots"><span></span><span></span><span></span><span></span><span></span><span></span><span></span><span></span><span></span></div>
  </div>
</div>

<h1 class="tagline">"The customer experience<br>application framework"</h1>

<div class="cta">
  <div class="cta-btn" style="left:0;width:112px">Live Demo</div>
  <div class="cta-btn" style="left:118px;width:60px">Buy</div>
  <p class="cta-note">30-day <u>FREE</u> trial for Panes OS<br>Also Available <u>For Orchard OS</u></p>
</div>

<div class="divider"></div>

<main class="features">
  <h2 class="feature-title lead">Creat compelling experiences for your customers</h2>
  <p class="feature-text">Lorem ipsum dolor sit amet, consec tetuer adipiscing elit. Praesent vestibulum molestie lacus. Aenean nonummy hen drerit mauris. Phasellus porta. Fusce suscipit varius mi. Cum sociis natoque read our.Lorem ipsum dolor sit amet, consec tetuer adipiscing elit. Praesent vestibulum molestie lacus. Aenean nonummy hen drerit mauris. Phasellus porta. Fusce suscipit varius mi. Cum sociis natoque read our.Lorem ipsum dolor sit amet, consec tetuer adipiscing elit. Praesent vestibulum molestie lacus. Aenean nonummy hen drerit mauris. Phasellus porta. Fusce suscipit varius mi. Cum sociis natoque read our.</p>
  <h2 class="feature-title sub">Opportunity through customer experience innovation</h2>
  <p class="feature-text">Lorem ipsum dolor sit amet, consec tetuer adipiscing elit. Praesent vestibulum molestie lacus. Aenean nonummy hen drerit mauris. Phasellus porta. Fusce suscipit varius mi. Cum sociis natoque read our.Lorem ipsum dolor sit amet, consec tetuer adipiscing elit. Praesent vestibulum molestie lacus. Aenean nonummy hen drerit mauris. Phasellus porta. Fusce suscipit varius mi. Cum sociis natoque read our.Lorem ipsum dolor sit amet, consec tetuer adipiscing elit. Praesent vestibulum molestie lacus. Aenean nonummy hen drerit mauris. Phasellus porta. Fusce suscipit varius mi. Cum sociis natoque read our.</p>
  <h2 class="feature-title sub">True difference</h2>
  <p class="feature-text">Lorem ipsum dolor sit amet, consec tetuer adipiscing elit. Praesent vestibulum molestie lacus. Aenean nonummy hen drerit mauris. Phasellus porta. Fusce suscipit varius mi. Cum sociis natoque read our.Lorem ipsum dolor sit amet, consec tetuer adipiscing elit. Praesent vestibulum molestie lacus. Aenean nonummy hen drerit mauris. Phasellus porta. Fusce suscipit varius mi. Cum sociis natoque read our.Lorem ipsum dolor sit amet, consec tetuer adipiscing elit. Praesent vestibulum molestie lacus. Aenean nonummy hen drerit mauris. Phasellus porta. Fusce suscipit varius mi. Cum sociis natoque read our.</p>
</main>

<footer class="site-footer">
  <div class="footer-col" style="left:42px">
    <h3>Vorlen</h3>
    <ul><li>Home</li><li>Products</li><li>Support</li><li>Blog</li><li>About</li></ul>
  </div>
  <div class="footer-col" style="left:202px">
    <h3>Getting Started</h3>
    <ul><li>Demo</li><li>Documentation</li><li>Download</li></ul>
  </div>
  <div class="footer-col" style="left:429px">
    <h3>Support</h3>
    <ul><li>Contact Us</li><li>Vorlen Services</li><li>Vorlen Support</li></ul>
  </div>
  <div class="footer-col" style="left:591px;width:260px">
    <h3>Subscribe to our newsletter</h3>
    <div class="subscribe-field">Email Address</div>
    <div class="subscribe-btn">Subscribe</div>
  </div>
  <div class="footer-col" style="left:969px">
    <h3>Follow Us</h3>
    <div class="social">
      <span class="social-link"><i></i>Linkfolk</span>
    </div>
    <div class="social" style="margin-top:6px">
      <span class="social-link"><i></i>Chatterbook</span>
    </div>
  </div>
</footer>
</body>
</html>
```